Klassisches Visitenkarten-Design mit braunen Farbtönen gesucht
Zielgruppe
Meine Firma bietet Pferdezahnbehandlungen, Pferdefütterungsberatung sowie Trensen- und Gebissanpassungen an. Ausserdem habe ich eine mobile Pferdewaage. Meine Kunden sind Pferdebesitzer der gehobenen Klasse, die gerne Geld in die Hand nehmen um ihr Tier korrekt zu halten/versorgen.
Ich setze bisher auf ein klassisches Design in braun Tönen.
Aufgabenstellung
Mir ist eine klare, schnörkellose Botschaft wichtig.
Ich möchte mich gerne mit klassischem, aber auch sehr schönem Design von der Konkurrenz abheben.
Der Fokus soll auf der wissenschaftlichen Arbeitsweise mit dem Partner Pferd liegen.
Im Anhang sind Fotos von der alten Visitenkarten. Dort fehlt mir aber die klare Linie.
Normalerweise arbeite ich mit der Schriftart Eurostyle, bin aber auch für neue Vorschläge offen.

```html
<!DOCTYPE html>
<html lang="de">
<head>
<meta charset="utf-8">
<title>Visitenkarte EQUIVANTA</title>
<link rel="stylesheet" href="https://fonts.googleapis.com/css2?family=Exo+2:wght@300;400;700&display=swap">
<style>
  :root {
    --page-bg: #ececec;
    --card-front: #ffffff;
    --card-back: #b99a80;
    --text-grey: #6f6f6f;
    --brown-dark: #552e10;
    --white: #ffffff;
  }
  * { margin: 0; padding: 0; box-sizing: border-box; }
  html, body { width: 1200px; height: 1200px; overflow: hidden; background: var(--page-bg); }
  body { position: relative; font-family: "Exo 2", sans-serif; color: var(--text-grey); }

  .card { position: absolute; left: 240px; width: 727px; height: 470px; }
  .card-front { top: 81px; background: var(--card-front); }
  .card-back { top: 647px; background: var(--card-back); }

  .brand-mark {
    position: absolute; left: 26px; top: 150px; width: 230px;
    display: flex; align-items: center; gap: 10px;
    color: var(--brown-dark); font-weight: 700; font-size: 30px; letter-spacing: 1px;
  }
  .brand-mark .dot { width: 22px; height: 22px; border-radius: 50%; background: var(--brown-dark); flex: none; }

  .contact { position: absolute; right: 42px; top: 0; text-align: right; line-height: 1; }
  .contact .name { position: absolute; right: 0; top: 104px; white-space: nowrap; font-weight: 700; font-size: 25px; }
  .contact .title-block { position: absolute; right: 0; top: 154px; white-space: nowrap; font-weight: 700; font-size: 20px; line-height: 24px; }
  .contact .address { position: absolute; right: 0; top: 217px; white-space: nowrap; font-weight: 300; font-size: 21px; line-height: 25px; font-style: normal; }
  .contact .reach { position: absolute; right: 0; top: 291px; white-space: nowrap; font-weight: 300; font-size: 21px; line-height: 24.5px; }

  .services {
    position: absolute; right: 42px; top: 400px; white-space: nowrap;
    font-weight: 700; font-size: 18px; letter-spacing: 0.2px;
  }

  .landscape-art {
    position: absolute; left: 43px; top: 19px; width: 643px; height: 284px;
    background: linear-gradient(180deg, rgba(255,255,255,0.18), rgba(255,255,255,0.06));
    border-radius: 4px;
  }
  .region {
    position: absolute; left: 42px; top: 346px; white-space: nowrap;
    color: var(--white); font-weight: 400; font-size: 52px; line-height: 1;
  }
  .brand-mark-back {
    position: absolute; left: 500px; top: 330px;
    display: flex; align-items: center; gap: 7px; white-space: nowrap;
    color: var(--white); font-weight: 700; font-size: 20px; letter-spacing: 1px;
  }
  .brand-mark-back .dot { width: 14px; height: 14px; border-radius: 50%; background: var(--white); flex: none; }
</style>
</head>
<body>
  <section class="card card-front">
    <div class="brand-mark"><span class="dot"></span>EQUIVANTA</div>
    <div class="contact">
      <h1 class="name">Marlene S. Kestner</h1>
      <p class="title-block">Agrarwissenschaften (Dr. sc.)<br>EQUIVANTA</p>
      <address class="address">Lindenweg 14<br>79999 Tannbach/Südschwarzwald</address>
      <p class="reach">Telefon: +49 (0) 170 - 5538192<br>E-Mail: kontakt@equiden-praxis.de<br>Internet: www.equivanta.de</p>
    </div>
    <p class="services">Pferdezahnbehandlung&nbsp; *&nbsp; Pferdefütterungsberatung&nbsp; *&nbsp; Pferdewaage</p>
  </section>

  <section class="card card-back">
    <div class="landscape-art" role="img" aria-label="Gezeichnete Hügellandschaft des Schwarzwalds mit Tannen in weißen Pinselstrichen"></div>
    <p class="region">Südschwarzwald</p>
    <div class="brand-mark-back"><span class="dot"></span>EQUIVANTA</div>
  </section>
</body>
</html>
```